Independence Day Graphics for Sale

I want to create 10 social media graphics (new Pictora size 4:5 (1080 x 1350 pixels) focusing on our July 4th Sale Graphics, using any of the pics attached. Use the attached pics, NO RANDOM STOCK PHOTOGRAPHY. For the color scheme of the graphics, they should all be complementary to the product colors in the photos.
You can add any of the photos attached but none are required. You can do some of the graphics in all text. I mainly need BOLD text that says one of the headlines (10 total) SEE ATTACHED WORD DOCUMENT for the headlines to use.

Target Market(s)

women looking to lose weight

Requirements
Must have
• pics attached and text attached

```html
<!DOCTYPE html>
<html lang="en">
<head>
<meta charset="utf-8">
<title>Biggest 4th of July Sale Ever</title>
<link rel="stylesheet" href="https://fonts.googleapis.com/css2?family=Anton&family=Playfair+Display:wght@900&family=Poppins:wght@700&display=swap">
<style>
  :root {
    --navy-deep: #0d1758;
    --navy: #1c2c8c;
    --navy-glow: #3447b8;
    --banner-blue: #2d3a9e;
    --headline-red: #f2343a;
    --flag-red: #c4161c;
    --white: #ffffff;
    --sparkle: #cfe0ff;
    --bottle-light: #f4f4f6;
    --bottle-shade: #d9dbe2;
  }
  html, body {
    margin: 0;
    padding: 0;
    overflow: hidden;
  }
  body {
    width: 960px;
    height: 1200px;
  }
  .sale-poster {
    position: relative;
    width: 960px;
    height: 1200px;
    overflow: hidden;
    background: radial-gradient(ellipse at 60% 40%, var(--navy-glow) 0%, var(--navy) 45%, var(--navy-deep) 100%);
  }
  .sky-sparkles {
    position: absolute;
    left: 0;
    top: 0;
  }
  .headline {
    position: absolute;
    left: 0;
    width: 100%;
    margin: 0;
    text-align: center;
    line-height: 1;
    white-space: nowrap;
  }
  .headline-top {
    top: -3px;
    left: -65px;
    font: 700 136px "Poppins", sans-serif;
    color: var(--white);
    letter-spacing: -1px;
  }
  .headline-holiday {
    top: 139px;
    font: 900 170px "Playfair Display", serif;
    color: var(--headline-red);
    letter-spacing: 6px;
  }
  .headline-bottom {
    top: 293px;
    left: -15px;
    font: 700 140px "Poppins", sans-serif;
    color: var(--white);
    letter-spacing: 0;
  }
  .product-row {
    position: absolute;
    top: 493px;
    left: 0;
    width: 960px;
    height: 300px;
  }
  .flag-stripes,
  .offer-banner {
    position: absolute;
    left: 0;
    top: 0;
  }
  .offer-text {
    position: absolute;
    left: 182px;
    width: 609px;
    margin: 0;
    text-align: center;
    font: 400 134px "Anton", sans-serif;
    color: var(--white);
    line-height: 1;
    letter-spacing: 2px;
  }
  .offer-amount { top: 838px; }
  .offer-scope { top: 975px; }
</style>
</head>
<body>
<main class="sale-poster">
  <svg class="sky-sparkles" width="960" height="1200" viewBox="0 0 960 1200" aria-hidden="true">
    <defs>
      <radialGradient id="sparkle-glow">
        <stop offset="0" stop-color="var(--sparkle)" stop-opacity="0.9"/>
        <stop offset="1" stop-color="var(--sparkle)" stop-opacity="0"/>
      </radialGradient>
    </defs>
    <g fill="url(#sparkle-glow)">
      <circle cx="396" cy="42" r="14"/>
      <circle cx="868" cy="108" r="12"/>
      <circle cx="40" cy="200" r="10"/>
      <circle cx="906" cy="322" r="12"/>
      <circle cx="112" cy="860" r="14"/>
      <circle cx="858" cy="820" r="12"/>
    </g>
    <g fill="var(--sparkle)">
      <circle cx="30" cy="20" r="3" opacity="0.8"/><circle cx="72" cy="48" r="2" opacity="0.6"/>
      <circle cx="118" cy="22" r="2.5" opacity="0.7"/><circle cx="160" cy="70" r="1.5" opacity="0.5"/>
      <circle cx="22" cy="96" r="2" opacity="0.6"/><circle cx="96" cy="120" r="3" opacity="0.7"/>
      <circle cx="210" cy="30" r="2" opacity="0.6"/><circle cx="268" cy="14" r="1.5" opacity="0.5"/>
      <circle cx="330" cy="44" r="2" opacity="0.7"/><circle cx="452" cy="18" r="2.5" opacity="0.6"/>
      <circle cx="520" cy="40" r="1.5" opacity="0.5"/><circle cx="590" cy="12" r="2" opacity="0.7"/>
      <circle cx="660" cy="30" r="1.5" opacity="0.5"/><circle cx="720" cy="58" r="2" opacity="0.6"/>
      <circle cx="792" cy="20" r="2.5" opacity="0.7"/><circle cx="840" cy="64" r="1.5" opacity="0.5"/>
      <circle cx="910" cy="30" r="2" opacity="0.6"/><circle cx="940" cy="160" r="2" opacity="0.6"/>
      <circle cx="900" cy="220" r="1.5" opacity="0.5"/><circle cx="60" cy="290" r="1.5" opacity="0.5"/>
      <circle cx="20" cy="380" r="2" opacity="0.6"/><circle cx="930" cy="420" r="1.5" opacity="0.5"/>
      <circle cx="40" cy="520" r="2" opacity="0.5"/><circle cx="920" cy="560" r="2" opacity="0.6"/>
      <circle cx="70" cy="640" r="1.5" opacity="0.5"/><circle cx="900" cy="680" r="2.5" opacity="0.6"/>
      <circle cx="30" cy="740" r="2" opacity="0.6"/><circle cx="60" cy="800" r="1.5" opacity="0.6"/>
      <circle cx="150" cy="820" r="2" opacity="0.7"/><circle cx="20" cy="860" r="2.5" opacity="0.7"/>
      <circle cx="90" cy="890" r="1.5" opacity="0.6"/><circle cx="140" cy="880" r="2" opacity="0.6"/>
      <circle cx="820" cy="800" r="2" opacity="0.6"/><circle cx="880" cy="760" r="1.5" opacity="0.6"/>
      <circle cx="930" cy="800" r="2.5" opacity="0.7"/><circle cx="840" cy="860" r="1.5" opacity="0.6"/>
      <circle cx="900" cy="880" r="2" opacity="0.7"/><circle cx="944" cy="900" r="1.5" opacity="0.6"/>
      <circle cx="810" cy="900" r="2" opacity="0.6"/><circle cx="870" cy="930" r="1.5" opacity="0.6"/>
    </g>
  </svg>

  <h1 class="headline headline-top">Biggest</h1>
  <p class="headline headline-holiday">4th of July</p>
  <p class="headline headline-bottom">Sale Ever!</p>

  <svg class="product-row" width="960" height="300" viewBox="0 493 960 300">
    <defs>
      <linearGradient id="bottle-fill" x1="0" x2="1" y1="0" y2="0">
        <stop offset="0" stop-color="var(--bottle-shade)"/>
        <stop offset="0.35" stop-color="var(--bottle-light)"/>
        <stop offset="1" stop-color="var(--bottle-shade)"/>
      </linearGradient>
    </defs>
    <rect role="img" aria-label="Photo of Liver Renew supplement bottle" x="132" y="494" width="165" height="294" rx="22" fill="url(#bottle-fill)"/>
    <rect role="img" aria-label="Photo of Gut Renew supplement bottle" x="320" y="498" width="151" height="290" rx="22" fill="url(#bottle-fill)"/>
    <rect role="img" aria-label="Photo of Balance Renew supplement bottle" x="498" y="498" width="155" height="290" rx="22" fill="url(#bottle-fill)"/>
    <rect role="img" aria-label="Photo of Glucose Renew supplement bottle" x="693" y="508" width="138" height="282" rx="22" fill="url(#bottle-fill)"/>
  </svg>

  <svg class="flag-stripes" width="960" height="1200" viewBox="0 0 960 1200" aria-hidden="true">
    <g fill="var(--flag-red)">
      <path d="M0 910 Q480 870 960 960 L960 985 Q480 895 0 935 Z"/>
      <path d="M0 960 Q480 920 960 1010 L960 1035 Q480 945 0 985 Z"/>
      <path d="M0 1010 Q480 970 960 1060 L960 1085 Q480 995 0 1035 Z"/>
      <path d="M0 1060 Q480 1020 960 1110 L960 1135 Q480 1045 0 1085 Z"/>
      <path d="M0 1110 Q480 1070 960 1160 L960 1185 Q480 1095 0 1135 Z"/>
      <path d="M0 1160 Q480 1120 960 1210 L960 1235 Q480 1145 0 1185 Z"/>
    </g>
    <g fill="var(--white)">
      <path d="M0 935 Q480 895 960 985 L960 1010 Q480 920 0 960 Z"/>
      <path d="M0 985 Q480 945 960 1035 L960 1060 Q480 970 0 1010 Z"/>
      <path d="M0 1035 Q480 995 960 1085 L960 1110 Q480 1020 0 1060 Z"/>
      <path d="M0 1085 Q480 1045 960 1135 L960 1160 Q480 1070 0 1110 Z"/>
      <path d="M0 1135 Q480 1095 960 1185 L960 1210 Q480 1120 0 1160 Z"/>
      <path d="M0 1185 Q480 1145 960 1235 L960 1260 Q480 1170 0 1210 Z"/>
    </g>
  </svg>

  <svg class="offer-banner" width="960" height="1200" viewBox="0 0 960 1200" aria-hidden="true">
    <path d="M206 827 H767 Q791 827 791 851 V1118 L484 1200 L182 1118 V851 Q182 827 206 827 Z" fill="var(--banner-blue)"/>
  </svg>

  <p class="offer-text offer-amount">25% OFF</p>
  <p class="offer-text offer-scope">SITEWIDE</p>
</main>
</body>
</html>
```